Redesign current business card for food company

i would like to redesign my business card. our company is food company, our product range from chips, juices, milk and etc (mostly dried food stuff).
I want o keep same logo but , the rest is open to new design.
you can check at our website about our company www.velqorafare.com

Target Market(s)

most of food company

Industry/Entity Type

Business

Contact Information for Business Card

I want to keep more to blue color...

Colors
3176b5
abd036

Requirements
Must have
• our old logo
Nice to have
• we do not mind to have nice material on bus card in order to accomplish nice design. for example: using spot uv, embossed and etc.

```html
<!DOCTYPE html>
<html lang="en">
<head>
<meta charset="utf-8">
<title>Velqorafare Business Card</title>
<link rel="stylesheet" href="https://fonts.googleapis.com/css2?family=Jost:wght@400;500;600&display=swap">
<style>
  :root {
    --brand-blue: #3176b5;
    --brand-green: #abd036;
    --ink: #1c1c1c;
    --text: #333a40;
    --paper: #ffffff;
    --backdrop: #eceef0;
  }
  * { box-sizing: border-box; margin: 0; padding: 0; }
  html, body {
    width: 1200px; height: 800px; overflow: hidden;
    background: var(--backdrop);
    font-family: "Jost", sans-serif;
  }
  .sheet {
    position: relative; width: 1200px; height: 800px;
    display: flex; align-items: center; justify-content: center; gap: 60px;
  }
  .card {
    position: relative; width: 520px; height: 300px;
    background: var(--paper); overflow: hidden;
    box-shadow: 0 6px 18px rgba(0,0,0,.12);
  }
  .card-shapes { position: absolute; inset: 0; width: 100%; height: 100%; }

  .wordmark { color: var(--brand-blue); font-weight: 600; letter-spacing: -0.5px; line-height: 1; }
  .card-front .wordmark { position: absolute; left: 60px; top: 105px; font-size: 54px; }
  .card-back .wordmark { position: absolute; left: 34px; top: 38px; font-size: 28px; }

  .holder { position: absolute; left: 34px; top: 145px; display: flex; align-items: center; gap: 12px; }
  .holder-name { color: var(--brand-blue); font-weight: 600; font-size: 17px; letter-spacing: 1px; text-transform: uppercase; line-height: 1.1; }
  .holder-role { color: var(--text); font-size: 10px; letter-spacing: 1px; text-transform: uppercase; }

  .icon-dot {
    width: 24px; height: 24px; border-radius: 50%;
    background: var(--brand-blue); display: flex; align-items: center; justify-content: center; flex: none;
  }
  .icon-dot svg { width: 13px; height: 13px; }

  .contact-list { position: absolute; left: 300px; top: 113px; display: flex; flex-direction: column; gap: 16px; }
  .contact-row { display: flex; align-items: center; gap: 10px; }
  .contact-lines { color: var(--text); font-size: 10.5px; line-height: 1.35; }

  .address { position: absolute; left: 165px; top: 238px; display: flex; align-items: center; gap: 10px; color: #f2f2f2; font-size: 11px; }
</style>
</head>
<body>
<main class="sheet">

  <section class="card card-front" aria-label="Card front">
    <svg class="card-shapes" viewBox="0 0 520 300" preserveAspectRatio="none" aria-hidden="true">
      <polygon points="0,272 250,232 250,244 0,284" fill="var(--brand-blue)"/>
      <path d="M238,236 Q246,222 264,219 L520,178 L520,212 L238,256 Z" fill="var(--ink)"/>
    </svg>
    <div class="wordmark">velqorafare</div>
  </section>

  <section class="card card-back" aria-label="Card back">
    <svg class="card-shapes" viewBox="0 0 520 300" preserveAspectRatio="none" aria-hidden="true">
      <polygon points="0,100 520,84 520,94 0,110" fill="var(--brand-blue)"/>
      <polygon points="0,268 160,262 156,278 0,284" fill="var(--brand-blue)"/>
      <path d="M150,236 Q154,222 172,221 L520,208 L520,262 L140,276 Z" fill="var(--ink)"/>
    </svg>

    <div class="wordmark">velqorafare</div>

    <div class="holder">
      <span class="icon-dot">
        <svg viewBox="0 0 16 16"><circle cx="8" cy="5" r="3" fill="#fff"/><path d="M2 15c0-4 3-5.5 6-5.5s6 1.5 6 5.5z" fill="#fff"/></svg>
      </span>
      <div>
        <div class="holder-name">Dara Welling</div>
        <div class="holder-role">Manager</div>
      </div>
    </div>

    <div class="contact-list">
      <div class="contact-row">
        <span class="icon-dot">
          <svg viewBox="0 0 16 16"><path d="M4 1.5l2.2 3-1.4 1.6c.8 1.8 2.3 3.3 4.1 4.1l1.6-1.4 3 2.2-1.3 2.6C6.8 13.2 2.8 9.2 1.4 3.7z" fill="#fff"/></svg>
        </span>
        <div class="contact-lines">Phone: 123456789<br>Fax: 123456789</div>
      </div>
      <div class="contact-row">
        <span class="icon-dot">
          <svg viewBox="0 0 16 16"><rect x="1.5" y="2.5" width="13" height="8.5" rx="1" fill="none" stroke="#fff" stroke-width="1.6"/><rect x="5" y="12.5" width="6" height="1.6" fill="#fff"/></svg>
        </span>
        <div class="contact-lines">dara.welling@website.com<br>www.velqorafare.com</div>
      </div>
    </div>

    <div class="address">
      <span class="icon-dot">
        <svg viewBox="0 0 16 16"><path d="M8 2l6 5.5h-2V14H4V7.5H2z" fill="#fff"/><rect x="6.6" y="9.5" width="2.8" height="4.5" fill="var(--brand-blue)"/></svg>
      </span>
      <span>Address Line, State, ZIP</span>
    </div>
  </section>

</main>
</body>
</html>
```